QM_radiance is a new upcoming amazing brand for modesty women , which started in 2016.

Design a page with all products and stating the title of the collection and style of the products and pricing.
Will need to create a column of upcoming events as well for customer to keep updated of our sales or flea
Updates

Target Market(s)

Hijabista, modesttrend

Number of Pages Required

5+ page

Requirements
Nice to have
• About Us
• Our brand represents classy and elegance yet it is comfortable and conservative to be worn everyday.
• Designs, and colours of fabrics chiffon , silk crepe and sateen silks and viscose cotton are exclusively chosen by QMradiance, imported from mainly high quality materials and sent for self manufactured.
• InsyaAllah#QMradiance

```html
<!DOCTYPE html>
<html lang="en">
<head>
<meta charset="utf-8">
<title>QM Radiance – Modest Wear</title>
<link rel="stylesheet" href="https://fonts.googleapis.com/css2?family=Montserrat:wght@400;500;600&family=Lato:wght@400;700&display=swap">
<style>
:root{
  --ink:#1b1b1b;
  --text:#3a3a3a;
  --muted:#777;
  --line:#c9c9c9;
  --hero:#ebd4c5;
  --card:#ececec;
  --panel:#e6e6e6;
  --footer:#222222;
  --footer-base:#1a1a1a;
  --footer-text:#9a9a9a;
  --white:#ffffff;
  --arrow-bg:#8a7f78;
}
*{margin:0;padding:0;box-sizing:border-box}
html,body{width:1200px;height:2826px;overflow:hidden;background:var(--white)}
body{position:relative;font-family:"Lato",sans-serif;color:var(--text)}
.abs{position:absolute}

/* top bar */
.topbar{left:0;top:0;width:1200px;height:36px;border-bottom:2px solid #bbb;font-size:11px;letter-spacing:.5px;color:#666}
.topbar span{position:absolute;top:11px}
/* header */
.logo{left:100px;top:50px;width:110px;text-align:center}
.logo-mark{width:56px;height:56px;margin:0 auto;border:2px solid var(--ink);display:flex;align-items:center;justify-content:center;font-family:"Montserrat",sans-serif;font-weight:600;font-size:20px;color:var(--ink)}
.logo-name{font-family:"Montserrat",sans-serif;font-weight:600;font-size:19px;color:var(--ink);margin-top:4px;white-space:nowrap}
.nav{top:124px;font-family:"Montserrat",sans-serif;font-size:12px;color:#333;letter-spacing:.4px}
.nav.active{font-weight:600;color:var(--ink)}
.search{left:842px;top:52px;width:188px;height:30px;border:1px solid #ccc;border-radius:15px;font-size:10px;color:#bbb;padding:8px 14px}
.search-btn{left:998px;top:52px;width:32px;height:30px;border-radius:15px;background:var(--ink)}
.cart{left:1045px;top:36px;width:57px;height:58px;background:var(--ink);color:#fff;font-size:10px;text-align:center;padding-top:24px;clip-path:polygon(0 0,100% 0,100% 100%,50% 85%,0 100%)}

/* hero */
.hero{left:0;top:160px;width:1200px;height:470px;background:var(--hero)}
.hero-photo{left:627px;top:160px;width:355px;height:470px;background:linear-gradient(160deg,#c67a78 0%,#4f7aa8 45%,#a2303a 80%,#e8cfc0 100%)}
.hero-title{left:100px;top:334px;font-family:"Montserrat",sans-serif;font-weight:600;font-size:33px;color:var(--ink);white-space:nowrap}
.hero-sub{left:100px;top:388px;font-family:"Montserrat",sans-serif;font-size:20px;letter-spacing:.6px;color:#2a2a2a;white-space:nowrap}
.btn-dark{left:102px;top:435px;width:115px;height:38px;background:var(--ink);color:#fff;font-size:11px;letter-spacing:.6px;display:flex;align-items:center;justify-content:center;font-family:"Montserrat",sans-serif}
.slide-arrow{top:362px;width:90px;height:43px;background:var(--arrow-bg);color:#fff;font-size:14px;font-family:"Montserrat",sans-serif;display:flex;align-items:center;justify-content:center;gap:8px}

/* section headings */
.sec-title{left:100px;font-family:"Montserrat",sans-serif;font-size:20px;color:#333;letter-spacing:.3px}
.sec-title b{font-weight:600;color:var(--ink)}
.sec-line{left:100px;width:1002px;height:2px;background:#aaa}
.pager{width:26px;height:26px;border:1px solid #ccc;border-radius:50%;background:#fff;display:flex;align-items:center;justify-content:center;font-size:12px;color:#333}

/* product cards */
.product-img{width:226px;height:210px;background:var(--card);display:flex;align-items:center;justify-content:center}
.product-img i{display:block;width:120px;height:170px;border-radius:50% 50% 10px 10px}
.p-name{font-size:12px;color:#555}
.p-price{font-family:"Montserrat",sans-serif;font-size:18px;font-weight:500;color:var(--ink)}
.p-cart{width:226px;height:30px;border-top:1px solid var(--line);border-bottom:1px solid var(--line);font-size:11px;letter-spacing:.6px;color:#333;display:flex;align-items:center;justify-content:center;font-family:"Montserrat",sans-serif}

/* welcome */
.welcome-panel{left:522px;top:1138px;width:678px;height:299px;background:var(--panel)}
.welcome-photo{left:9px;top:1111px;width:513px;height:344px;background:linear-gradient(120deg,#9fb0c2 0%,#dfe5ec 40%,#f0d6c4 60%,#8c9aa8 100%)}
.welcome-frame{left:9px;top:1120px;width:503px;height:326px;border:1.5px solid #333}
.welcome-title{left:555px;top:1168px;font-family:"Montserrat",sans-serif;font-size:24px;color:#333;white-space:nowrap}
.welcome-title b{font-weight:600;color:var(--ink)}
.welcome-text{left:555px;top:1226px;width:550px;font-size:13px;line-height:29.6px;color:#333}
.read-more{left:557px;top:1387px;font-size:13px;font-weight:700;color:var(--ink)}

/* tabs */
.tab-active{left:100px;top:1522px;width:208px;height:40px;background:var(--ink);color:#fff;font-family:"Montserrat",sans-serif;font-size:19px;display:flex;align-items:center;justify-content:center}
.tab{left:330px;top:1529px;font-family:"Montserrat",sans-serif;font-size:19px;color:#333}
.tab b{font-weight:600;color:var(--ink)}

/* events */
.event-img{top:2014px;width:480px;height:172px}
.date-badge{top:2127px;width:60px;height:59px;background:#222;color:#fff;text-align:center;font-family:"Montserrat",sans-serif;padding-top:8px}
.date-badge .d{font-size:19px;line-height:20px}
.date-badge .m{font-size:12px;margin-top:4px}
.event-text{top:2202px;width:480px;font-size:13px;line-height:26px;color:#333}
.btn-outline{top:2268px;width:170px;height:36px;border:1px solid #444;font-size:12px;color:#333;display:flex;align-items:center;justify-content:center;gap:14px}

/* features */
.feature{top:2366px;width:318px;height:104px;background:#efefef;display:flex;align-items:center;justify-content:center}
.feature-label{top:2487px;width:318px;text-align:center;font-family:"Montserrat",sans-serif;font-size:14px;color:#222;letter-spacing:.4px}

/* footer */
.footer{left:0;top:2541px;width:1200px;height:210px;background:var(--footer)}
.footer-base{left:0;top:2751px;width:1200px;height:75px;background:var(--footer-base)}
.f-head{top:2570px;font-family:"Montserrat",sans-serif;font-size:12px;font-weight:600;color:#fff;letter-spacing:.5px}
.f-list{top:2604px;list-style:none;font-size:11px;color:var(--footer-text);line-height:25.6px}
.f-list li::before{content:"";display:inline-block;width:6px;height:6px;border:1px solid var(--footer-text);transform:rotate(45deg);margin-right:9px;vertical-align:1px}
.f-copy{font-size:11px;line-height:17px;color:var(--footer-text)}
.news-input{left:588px;top:2662px;width:235px;height:27px;border-radius:14px;background:#fff;font-size:9px;color:#aaa;padding:8px 14px}
.news-btn{left:795px;top:2664px;width:24px;height:23px;border-radius:12px;background:#666}
.social{top:2660px;width:30px;height:30px;border-radius:50%;background:#555}
.pay{top:2788px;font-size:10px;font-weight:700;color:#e0e0e0}
</style>
</head>
<body>

<!-- top bar -->
<div class="abs topbar">
  <span style="left:100px">MY ACCOUNT</span>
  <span style="left:195px;color:#bbb">|</span>
  <span style="left:217px">WISH LIST (0)</span>
  <span style="left:305px;color:#bbb">|</span>
  <span style="left:327px">CHECKOUT</span>
  <span style="left:971px">LOGIN</span>
  <span style="left:1021px;color:#bbb">|</span>
  <span style="left:1045px">REGISTER</span>
</div>

<!-- header -->
<div class="abs logo">
  <div class="logo-mark">QM</div>
  <div class="logo-name">QM Radiance</div>
</div>
<div class="abs nav active" style="left:523px">HOME</div>
<div class="abs nav" style="left:636px">ABOUT US</div>
<div class="abs nav" style="left:771px">PRODUCTS</div>
<div class="abs nav" style="left:912px">EVENTS</div>
<div class="abs nav" style="left:1021px">CONTACT US</div>

<div class="abs search">Search...</div>
<div class="abs search-btn">
  <svg width="32" height="30" viewBox="0 0 32 30"><circle cx="15" cy="14" r="4.5" fill="none" stroke="#fff" stroke-width="1.8"/><line x1="18.5" y1="17.5" x2="21.5" y2="20.5" stroke="#fff" stroke-width="2"/></svg>
</div>
<div class="abs cart">
  <svg class="abs" style="left:20px;top:6px" width="18" height="15" viewBox="0 0 18 15"><path d="M1 2h3l2 8h9l2-6H5" fill="none" stroke="#fff" stroke-width="1.4"/><circle cx="7" cy="13" r="1.3" fill="#fff"/><circle cx="14" cy="13" r="1.3" fill="#fff"/></svg>
  (0) Item
</div>

<!-- hero -->
<div class="abs hero"></div>
<div class="abs hero-photo" role="img" aria-label="Woman in a floral hijab, denim shirt and red skirt"></div>
<div class="abs hero-title">Wide Range Of Branded</div>
<div class="abs hero-sub">CLOTH FOR MODESTY &amp; HIJAAB WOMAN</div>
<div class="abs btn-dark">SHOP NOW</div>
<div class="abs slide-arrow" style="left:0"><span>&#10229;</span>Prev</div>
<div class="abs slide-arrow" style="left:1110px">Next<span>&#10230;</span></div>

<!-- our collections -->
<div class="abs sec-title" style="top:696px">OUR <b>COLLECTIONS</b></div>
<div class="abs sec-line" style="top:730px"></div>
<div class="abs pager" style="left:1043px;top:696px">&lsaquo;</div>
<div class="abs pager" style="left:1077px;top:696px">&rsaquo;</div>

<div class="abs product-img" style="left:100px;top:755px" role="img" aria-label="Model wearing a dark floral hijab"><i style="background:linear-gradient(#8b8f6a,#2c2c2c)"></i></div>
<div class="abs product-img" style="left:362px;top:755px" role="img" aria-label="Model wearing a peach printed hijab"><i style="background:linear-gradient(#f3c3a3,#2c2c2c)"></i></div>
<div class="abs product-img" style="left:622px;top:755px" role="img" aria-label="Folded printed scarves in pink and dark patterns"><i style="width:160px;height:110px;border-radius:6px;background:linear-gradient(90deg,#d7a4b5,#f4b9a7 40%,#2f3a2c 60%,#5a5f3a)"></i></div>
<div class="abs product-img" style="left:876px;top:755px" role="img" aria-label="Model wearing a light patterned hijab"><i style="background:linear-gradient(#c9d2d6,#2c2c2c)"></i></div>

<div class="abs p-name" style="left:100px;top:984px">Lorem Ips Dolamet</div>
<div class="abs p-price" style="left:260px;top:980px">$07.56</div>
<div class="abs p-name" style="left:366px;top:984px">Aorepsum Dolamet</div>
<div class="abs p-price" style="left:522px;top:980px">$22.56</div>
<div class="abs p-name" style="left:622px;top:984px">Bdm Ipsu Dolamet</div>
<div class="abs p-price" style="left:789px;top:980px">$105.0</div>
<div class="abs p-name" style="left:880px;top:984px">Voem Ipsum Dolat</div>
<div class="abs p-price" style="left:1039px;top:980px">$28.56</div>

<div class="abs p-cart" style="left:100px;top:1017px">+&nbsp; ADD TO CART</div>
<div class="abs p-cart" style="left:362px;top:1017px">+&nbsp; ADD TO CART</div>
<div class="abs p-cart" style="left:622px;top:1017px">+&nbsp; ADD TO CART</div>
<div class="abs p-cart" style="left:876px;top:1017px">+&nbsp; ADD TO CART</div>

<!-- welcome -->
<div class="abs welcome-panel"></div>
<div class="abs welcome-photo" role="img" aria-label="Woman in navy hijab and blush cape on a city rooftop"></div>
<div class="abs welcome-frame"></div>
<div class="abs welcome-title">WELCOME TO <b>QM RADIANCE EXCLUSIVE</b></div>
<p class="abs welcome-text">Lorem ipsum dolor sit amet, consectetuer adipiscing elit, sed diam nonummy nibh euismod tincidunt ut laoreet dolore magna aliquam erat volutpat. Ut wisi enim ad minim veniam, quis nostrud exerci tation ullamcorper suscipit lobortis nisl ut aliquip ex ea commodo consequat, vel illum dolore eu feugiat nulla facilisis at vero eros et accumsan et iusto odio dignissim qui blandit praesent lulla facilisi.</p>
<div class="abs read-more">Read More &nbsp;&#10230;</div>

<!-- latest product / on sale -->
<div class="abs tab-active">LATEST PRODUCT</div>
<div class="abs tab">ON <b>SALE</b></div>
<div class="abs sec-line" style="top:1562px"></div>
<div class="abs pager" style="left:1043px;top:1527px">&lsaquo;</div>
<div class="abs pager" style="left:1077px;top:1527px">&rsaquo;</div>

<div class="abs product-img" style="left:100px;top:1586px" role="img" aria-label="Folded pink and crimson embellished scarves"><i style="width:130px;height:110px;border-radius:4px;background:linear-gradient(90deg,#f2b9c8 50%,#9c1d3c 50%)"></i></div>
<div class="abs product-img" style="left:362px;top:1586px" role="img" aria-label="Teal scarf with floral appliqué and cord"><i style="width:150px;height:110px;border-radius:6px;background:linear-gradient(#3aa596,#2b8f82)"></i></div>
<div class="abs product-img" style="left:622px;top:1586px" role="img" aria-label="Model wearing a dark floral hijab"><i style="background:linear-gradient(#8b8f6a,#2c2c2c)"></i></div>
<div class="abs product-img" style="left:876px;top:1586px" role="img" aria-label="Folded printed scarves in pink and dark patterns"><i style="width:160px;height:110px;border-radius:6px;background:linear-gradient(90deg,#d7a4b5,#f4b9a7 40%,#2f3a2c 60%,#5a5f3a)"></i></div>

<div class="abs p-name" style="left:100px;top:1816px">Lorem Ips Dolamet</div>
<div class="abs p-price" style="left:260px;top:1812px">$07.56</div>
<div class="abs p-name" style="left:366px;top:1816px">Aorepsum Dolamet</div>
<div class="abs p-price" style="left:522px;top:1812px">$22.56</div>
<div class="abs p-name" style="left:622px;top:1816px">Bdm Ipsu Dolamet</div>
<div class="abs p-price" style="left:789px;top:1812px">$105.0</div>
<div class="abs p-name" style="left:880px;top:1816px">Voem Ipsum Dolat</div>
<div class="abs p-price" style="left:1039px;top:1812px">$28.56</div>

<div class="abs p-cart" style="left:100px;top:1848px">+&nbsp; ADD TO CART</div>
<div class="abs p-cart" style="left:362px;top:1848px">+&nbsp; ADD TO CART</div>
<div class="abs p-cart" style="left:622px;top:1848px">+&nbsp; ADD TO CART</div>
<div class="abs p-cart" style="left:876px;top:1848px">+&nbsp; ADD TO CART</div>

<!-- upcoming events -->
<div class="abs sec-title" style="top:1946px">UPCOMING <b>EVENTS</b></div>
<div class="abs sec-line" style="top:1977px"></div>
<div class="abs pager" style="left:1043px;top:1945px">&lsaquo;</div>
<div class="abs pager" style="left:1077px;top:1945px">&rsaquo;</div>

<div class="abs event-img" style="left:100px;background:linear-gradient(90deg,#b49a7c,#d7c3a8 40%,#2a2a2a 60%,#8a6a4c)" role="img" aria-label="Woman in black hijab against a wooden wall"></div>
<div class="abs event-img" style="left:622px;background:linear-gradient(90deg,#6b8f3a,#e8dcc0 35%,#7aa34a 70%,#3f5a2a)" role="img" aria-label="Woman in cream hijab in a sunny park"></div>
<div class="abs date-badge" style="left:100px"><div class="d">17</div><div class="m">JUNE</div></div>
<div class="abs date-badge" style="left:622px"><div class="d">17</div><div class="m">JUNE</div></div>
<p class="abs event-text" style="left:100px">lobortis nisl ut aliquip ex ea commodo consequat. Duis autem vel eum iriure dolor in hendrerit inilore eu feugiat nulla facilisis at vero..</p>
<p class="abs event-text" style="left:622px">lobortis nisl ut aliquip ex ea commodo consequat. Duis autem vel eum iriure dolor in hendrerit in vulpue molestie ct, velo..</p>
<div class="abs btn-outline" style="left:100px">Continue Reading <span>&#10230;</span></div>
<div class="abs btn-outline" style="left:622px">Continue Reading <span>&#10230;</span></div>

<!-- features -->
<div class="abs feature" style="left:100px">
  <svg width="112" height="50" viewBox="0 0 112 50" fill="none" stroke="#333" stroke-width="1.6">
    <rect x="2" y="4" width="74" height="34"/>
    <path d="M76 14h18l14 13v11H76z"/>
    <circle cx="22" cy="42" r="6" fill="#efefef"/><circle cx="92" cy="42" r="6" fill="#efefef"/>
    <text x="39" y="26" font-family="Montserrat,sans-serif" font-size="12" fill="#333" stroke="none" text-anchor="middle" font-weight="600">FREE!</text>
  </svg>
</div>
<div class="abs feature" style="left:439px">
  <svg width="86" height="60" viewBox="0 0 86 60" fill="none" stroke="#333" stroke-width="1.6">
    <rect x="2" y="8" width="82" height="50"/>
    <path d="M55 8 L48 1 M55 8 L62 1"/>
    <line x1="55" y1="8" x2="55" y2="58"/>
    <text x="28" y="42" font-family="Montserrat,sans-serif" font-size="24" fill="#333" stroke="none" text-anchor="middle">$</text>
  </svg>
</div>
<div class="abs feature" style="left:782px">
  <svg width="70" height="70" viewBox="0 0 70 70" fill="none" stroke="#333" stroke-width="1.6">
    <circle cx="35" cy="30" r="17" fill="#333"/>
    <path d="M14 32 a21 21 0 0 1 42 0"/>
    <rect x="10" y="28" width="7" height="14" fill="#333"/><rect x="53" y="28" width="7" height="14" fill="#333"/>
    <path d="M56 42 q0 12 -14 14"/>
    <path d="M14 68 q21 -22 42 0" fill="#333"/>
  </svg>
</div>
<div class="abs feature-label" style="left:100px">FREE SHIPPING</div>
<div class="abs feature-label" style="left:439px">SPECIAL GIFT CARDS</div>
<div class="abs feature-label" style="left:782px">24/7 CUSTOMER CARE</div>

<!-- footer -->
<div class="abs footer"></div>
<div class="abs footer-base"></div>

<div class="abs f-head" style="left:100px">INFORMATION</div>
<ul class="abs f-list" style="left:100px"><li>About Us</li><li>Delivery</li><li>Information</li><li>Privacy Policy</li><li>Terms &amp; Condition</li></ul>
<div class="abs f-head" style="left:252px">CUSTOMER SERVICE</div>
<ul class="abs f-list" style="left:252px"><li>Contact Us</li><li>Orders</li><li>Returns</li><li>Site Map</li></ul>
<div class="abs f-head" style="left:435px">EXTRAS</div>
<ul class="abs f-list" style="left:435px"><li>Brands</li><li>Vouchers</li><li>Affiliates</li><li>Specials</li></ul>

<div class="abs f-head" style="left:588px">NEWSLETTER</div>
<p class="abs f-copy" style="left:588px;top:2604px;width:260px">Sincidunt ut laoreet dolore magna aliquam erat volutpost ullamcr suscipit ...</p>
<div class="abs news-input">Send us your email...</div>
<div class="abs news-btn">
  <svg width="24" height="23" viewBox="0 0 24 23"><rect x="6.5" y="7.5" width="11" height="8" fill="none" stroke="#fff"/><path d="M6.5 7.5l5.5 4.5 5.5-4.5" fill="none" stroke="#fff"/></svg>
</div>

<div class="abs f-head" style="left:876px">FOLLOW US</div>
<p class="abs f-copy" style="left:876px;top:2604px;width:240px">Sincidunt ut laoreet dolore magna aliquam erat volutpostrud ullamcr suscipit</p>
<div class="abs social" style="left:880px"></div>
<div class="abs social" style="left:924px"></div>
<div class="abs social" style="left:968px"></div>
<div class="abs social" style="left:1012px"></div>

<div class="abs f-copy" style="left:105px;top:2778px">All Rights Reserved ©qmradiance.com</div>
<div class="abs f-copy" style="left:933px;top:2762px">Accepted Payment</div>
<div class="abs pay" style="left:918px">Orvane</div>
<div class="abs pay" style="left:963px">Paquilo</div>
<div class="abs pay" style="left:1010px">Velmora</div>
<div class="abs pay" style="left:1062px">Truxa</div>

</body>
</html>
```